Pipelining Product Supply Company Needs New Stationery

We need new stationery (letter head, with compliments slips & business card) for our industry leading pipe lining supply company. basically we sell product to other plumbers to carry out pipe relining.

Im looking for something, fresh, professional, sleek and modern at the same time.

Ive attached a copy of the logo and also some guidelines to follow for colours and fonts etc.

Target Market(s)

Plumbers

Industry/Entity Type

Plumbing

Font styles to use
Sans Serif

Requirements
Must have
• The logo, space for ABN, Address, Phone Number, website and email.
Nice to have
• Stand out from the crowd. To look sleep and professional.
Should not have
• Any other colours apart from what is on the guidelines.

```html
<!DOCTYPE html>
<html lang="en">
<head>
<meta charset="utf-8">
<title>Tideline Pipe Supply – Business Card</title>
<link rel="stylesheet" href="https://fonts.googleapis.com/css2?family=Questrial&display=swap">
<style>
  :root {
    --page-bg: #d9d6d1;
    --card-light: #f1f1ef;
    --card-mid: #dcdddb;
    --brand-green: #3f8a2a;
    --band-dark: #1c4f1a;
    --band-light: #3d7d2c;
    --name-text: #eaf2dc;
    --detail-text: #e9d8c8;
  }
  * { margin: 0; padding: 0; box-sizing: border-box; }
  html, body {
    width: 1200px;
    height: 969px;
    overflow: hidden;
    background: var(--page-bg);
    font-family: "Questrial", "Century Gothic", sans-serif;
  }
  .canvas {
    position: relative;
    width: 1200px;
    height: 969px;
  }
  .business-card {
    position: absolute;
    left: 100px;
    top: 200px;
    width: 1000px;
    height: 570px;
    background: linear-gradient(160deg, var(--card-light) 0%, var(--card-mid) 100%);
    border: 1px solid #c9cac7;
    overflow: hidden;
    box-shadow: 0 12px 30px rgba(0,0,0,0.18);
  }
  .brand {
    position: absolute;
    top: 130px;
    left: 0;
    width: 100%;
    display: flex;
    justify-content: center;
    align-items: center;
    gap: 22px;
  }
  .brand-mark {
    width: 46px;
    height: 46px;
    background: var(--brand-green);
  }
  .brand-name {
    font-size: 64px;
    color: var(--brand-green);
    letter-spacing: 1px;
  }
  .contact-band {
    position: absolute;
    left: 0;
    top: 352px;
    width: 1000px;
    height: 218px;
    background: linear-gradient(180deg, var(--band-light) 0%, var(--band-dark) 100%);
    border-top-right-radius: 70px;
    color: var(--detail-text);
    text-align: center;
    padding-top: 30px;
  }
  .person {
    font-size: 32px;
    color: var(--name-text);
    margin-bottom: 16px;
  }
  .person .role {
    font-size: 22px;
    letter-spacing: 1px;
  }
  .details {
    font-size: 23px;
    line-height: 1.5;
  }
  .website {
    font-size: 22px;
    letter-spacing: 2px;
  }
</style>
</head>
<body>
<div class="canvas">
  <div class="business-card">
    <div class="brand">
      <span class="brand-mark"></span>
      <span class="brand-name">Tideline Pipe Supply</span>
    </div>
    <div class="contact-band">
      <p class="person">MARCUS HALE <span class="role">- PRESIDENT</span></p>
      <p class="details">2710 Harbour Street, Lakemont, NY 10290</p>
      <p class="details">ABN: 4471902836 | (P) 555 0142 7790 &nbsp;(E) hello@tidelinesupply.com</p>
      <p class="website">www.tidelinepipesupply.com</p>
    </div>
  </div>
</div>
</body>
</html>
```